Meadowlark Archive needs a Business Card

Designers!
More often than not, people want a cheap business card and often argue "I only want 100, not 500" - Years ago I worked in print and always wanted a client to ask for something that challenged me and would be great for my portfolio.

Years have past, and I dont have the time to do it myself so I'd love to see what everyone can offer.

Reason: Hey Guys, The designs are looking good but i've extended it a few more days as I wont be near a laptop and i'm trying to provide everyone feedback - Sorry!

Target Market(s)

Key decision makers, Potential Clients, Networking events and opportunities.

Industry/Entity Type

Business

Requirements
Must have
• Typography is very important. The type of paper is important.
The print, the shape. The creativity.
I'm very inspired by the below link
http://www.vornelby.com/blog/business-card-design/

Nice to have
• Stencelled cutouts. Embossing, nice typography.
I'd like the business card to be a conversation piece itself.

Attached is an image of business cards i've had in the past.
Additionally, some logos i've recently had designed by CraftQuarry.

```html
<!DOCTYPE html>
<html lang="en">
<head>
<meta charset="utf-8">
<title>Meadowlark Archive – Business Card</title>
<link rel="stylesheet" href="https://fonts.googleapis.com/css2?family=Source+Sans+3:wght@400;600&family=Questrial&display=swap">
<style>
  :root {
    --stage: #e4e4e2;
    --card-blue: #0e2c78;
    --beam-light: rgba(150, 185, 235, 0.28);
    --beam-green: rgba(140, 190, 140, 0.35);
    --band-green: #4d8a45;
    --band-green-light: #7fb465;
    --accent-green: #7cc242;
    --text-white: #ffffff;
  }
  * { box-sizing: border-box; margin: 0; padding: 0; }
  html, body { width: 1200px; height: 716px; overflow: hidden; background: var(--stage); }
  .canvas {
    position: relative; width: 1200px; height: 716px;
    display: flex; align-items: center; justify-content: center; gap: 50px;
  }
  .card {
    position: relative; width: 500px; height: 290px;
    background: var(--card-blue); overflow: hidden;
    color: var(--text-white);
    font-family: "Source Sans 3", sans-serif;
  }
  .card-art { position: absolute; inset: 0; width: 100%; height: 100%; }
  .card-content { position: absolute; inset: 0; }

  /* Front */
  .front .brand {
    position: absolute; left: 0; right: 0; top: 100px; text-align: center;
  }
  .brand-name {
    display: inline-flex; align-items: center; gap: 12px;
    font-size: 30px; font-weight: 400; letter-spacing: 1px; line-height: 1;
  }
  .brand-square { width: 26px; height: 26px; background: var(--text-white); }
  .front .site {
    margin-top: 22px;
    font-family: "Questrial", sans-serif;
    font-size: 15px; letter-spacing: 5px; color: var(--accent-green);
  }

  /* Back */
  .back .mini-brand { position: absolute; left: 24px; top: 20px; }
  .back .mini-brand .brand-name { font-size: 14px; gap: 6px; letter-spacing: 0.5px; }
  .back .mini-brand .brand-square { width: 12px; height: 12px; }
  .back .mini-site {
    margin-top: 4px; font-family: "Questrial", sans-serif;
    font-size: 7px; letter-spacing: 2px; color: var(--accent-green);
  }
  .back .holder { position: absolute; left: 30px; top: 76px; }
  .holder-name { font-size: 24px; font-weight: 400; margin-bottom: 12px; }
  .contact-list { list-style: none; font-size: 12px; line-height: 1.55; }
</style>
</head>
<body>
<main class="canvas">

  <section class="card front" aria-label="Card front">
    <svg class="card-art" viewBox="0 0 500 290" preserveAspectRatio="none" aria-hidden="true">
      <polygon points="0,0 70,0 20,130 0,150" fill="var(--beam-light)"/>
      <polygon points="300,0 360,0 500,200 500,260" fill="var(--beam-green)"/>
      <polygon points="380,0 420,0 500,110 500,160" fill="var(--beam-light)"/>
      <polygon points="230,190 500,230 500,270 260,230" fill="var(--beam-green)"/>
      <polygon points="0,250 220,270 0,275" fill="var(--beam-light)"/>
      <polygon points="0,268 500,260 500,290 0,290" fill="var(--band-green)"/>
      <polygon points="0,270 260,262 200,290 0,290" fill="var(--band-green-light)" opacity="0.6"/>
    </svg>
    <div class="card-content">
      <div class="brand">
        <div class="brand-name"><span class="brand-square"></span>MEADOWLARK ARCHIVE</div>
        <p class="site">meadowlarkarchive.com.au</p>
      </div>
    </div>
  </section>

  <section class="card back" aria-label="Card back">
    <svg class="card-art" viewBox="0 0 500 290" preserveAspectRatio="none" aria-hidden="true">
      <polygon points="0,100 40,140 130,290 60,290 0,190" fill="var(--beam-light)"/>
      <polygon points="320,90 360,90 460,290 420,290" fill="var(--beam-green)"/>
      <polygon points="400,60 430,60 500,200 500,260" fill="var(--beam-light)"/>
      <polygon points="300,200 500,150 500,200 330,230" fill="var(--beam-green)"/>
      <polygon points="0,230 500,275 500,290 0,290" fill="var(--band-green)"/>
      <polygon points="0,240 300,262 260,290 0,290" fill="var(--band-green-light)" opacity="0.6"/>
    </svg>
    <div class="card-content">
      <div class="mini-brand">
        <div class="brand-name"><span class="brand-square"></span>MEADOWLARK ARCHIVE</div>
        <p class="mini-site">k4studio.com.au</p>
      </div>
      <div class="holder">
        <h1 class="holder-name">Daniel Hartley</h1>
        <ul class="contact-list">
          <li>Phone: 38650147</li>
          <li>Fax: 38650148</li>
          <li>Email: daniel@k4studio.au</li>
          <li>www.k4studio.com.au</li>
        </ul>
      </div>
    </div>
  </section>

</main>
</body>
</html>
```